IT company developing solutions for air cargo industry is looking for a new website

We are a professional IT company developing solutions for air cargo industry worldwide.

We are looking to update and completely redesign our current webpages: https://www.brixtonvale.cz/

What we like about our current pages are the animated graphics on the home page. These could stay, but not a must.

The design of the new pages should be very modern, clean, unique, creative, professional, and to make a statement. We are looking for animated graphics, cool and interesting interactions, cascading layers, etc.

Our company logo is yellow, gray and black. You don’t necessarily have to stick to this colour scheme, however the corporate colors should work well with the overal design of the web pages.
Dark mode pages are also an option.

The scope of the project would include creating a:

• Header
• Footer
• Landing page
• Navigation bar (8 tabs)
• Subpages (10)

In the first stage we are looking only for the header / footer / landing page with navigaton bar / Solutions page design.
As a second round, finalists might be asked to submit another section of the website to see their consistency in terms of the look and feel proposed for the Homepage and Solutions’ pages.
The winning designer will then complete the rest of the pages.

Attached you will find a brief for the first scope of the project. Please read the note section on slide nr. 3 carefully to understand, what we exactly are looking for to achieve.

Industry/Entity Type

Aviation

Number of Pages Required

1 page

Requirements
Must have
• See brief
Nice to have
• See brief
Should not have
• See brief

```html
<!DOCTYPE html>
<html lang="en">
<head>
<meta charset="utf-8">
<title>Brixton Vale – IT solutions for air cargo</title>
<link href="https://fonts.googleapis.com/css2?family=Poppins:wght@300;400;500;600;700&display=swap" rel="stylesheet">
<style>
:root{
  --gold:#f7c600;
  --black:#000;
  --night:#0b0b0d;
  --panel:#111114;
  --white:#fff;
  --grey:#bdbdbd;
  --line:#3a3a3a;
}
*{box-sizing:border-box;margin:0;padding:0}
html,body{width:1200px;height:3096px;overflow:hidden;background:var(--black);font-family:'Poppins',sans-serif;color:var(--white)}
.page{position:relative;width:1200px;height:3096px}
.topbar{height:28px;background:var(--gold);color:#111;font-size:13px;font-weight:600;display:flex;align-items:center;justify-content:center}
.brand{display:flex;align-items:center;gap:12px;font-size:26px;font-weight:600;color:var(--white)}
.brand-mark{width:36px;height:36px;background:var(--gold)}
.header{position:absolute;top:28px;left:0;width:1200px;height:100px;display:flex;align-items:center;justify-content:space-between;padding:0 88px 0 112px;z-index:2}
.btn-outline{border:2px solid var(--white);padding:12px 22px;font-size:14px;font-weight:600;color:var(--white)}
.nav{position:absolute;top:130px;left:112px;width:980px;height:52px;background:var(--gold);border-radius:8px;display:flex;align-items:center;justify-content:space-between;padding:0 26px 0 12px;z-index:2}
.nav a{font-size:13px;font-weight:600;color:#111;text-decoration:none}
.nav a.active{background:#111;color:var(--white);padding:7px 16px;border-radius:16px}
.hero{position:absolute;top:28px;left:0;width:1200px;height:900px;background:radial-gradient(circle at 80% 30%,#1a2a44 0%,#0a0e18 40%,#050608 75%)}
.earth{position:absolute;left:660px;top:150px;width:520px;height:520px;border-radius:50%;background:radial-gradient(circle at 40% 40%,#2f6ea8 0%,#163a66 45%,#07182e 80%);box-shadow:0 0 50px rgba(80,150,255,.45)}
.hero-copy{position:absolute;left:112px;top:240px;width:480px}
.hero h1{font-size:34px;line-height:1.3;font-weight:700}
.hero h1 em{font-style:normal;color:var(--gold)}
.hero p{margin-top:22px;font-size:14px;line-height:1.6;color:#ddd}
.btn-gold{display:inline-block;background:var(--gold);color:#111;font-size:13px;font-weight:600;padding:14px 22px}
.hero .btn-gold{margin-top:30px}
.play{position:absolute;left:112px;top:650px;width:80px;height:80px;border:4px solid var(--gold);border-radius:50%;display:flex;align-items:center;justify-content:center}
.play-label{position:absolute;left:112px;top:750px;font-size:18px;font-weight:500;text-decoration:underline}
.statement{position:absolute;top:995px;left:0;width:1200px;text-align:center;font-size:24px;font-weight:600;line-height:1.5}
.facts-title{position:absolute;top:1120px;left:0;width:1200px;text-align:center;font-size:44px;font-weight:400}
.facts{position:absolute;top:1220px;left:180px;width:840px;display:grid;grid-template-columns:1fr 1fr;row-gap:56px}
.facts::after{content:"";position:absolute;left:425px;top:0;width:1px;height:360px;background:var(--line)}
.fact{padding-left:0}
.fact:nth-child(even){padding-left:500px;margin-left:-410px}
.fact b{display:block;font-size:44px;font-weight:600;color:var(--gold);line-height:1.1}
.fact span{display:block;font-size:20px;margin-top:6px}
.iso-art{position:absolute;top:1620px;left:0;width:1200px;height:760px;background:radial-gradient(ellipse at 30% 45%,#1c2236 0%,#0d0f18 45%,#000 80%)}
.about{position:absolute;top:1735px;left:590px;width:460px}
.about h2{font-size:36px;font-weight:400}
.about h2 strong{font-weight:700}
.about p{margin-top:28px;font-size:16px;line-height:1.65;text-align:justify}
.about .btn-gold{margin-top:34px}
.solutions-title{position:absolute;top:2340px;left:0;width:1200px;text-align:center;font-size:34px;font-weight:400}
.solutions-title strong{font-weight:700}
.products{position:absolute;top:2515px;left:100px;width:1000px;display:flex;justify-content:space-between}
.product{width:180px;text-align:center}
.product-icon{width:152px;height:152px;margin:0 auto;border-radius:50%;background:var(--white);border:9px solid var(--gold);display:flex;align-items:center;justify-content:center}
.product-icon.alt{border-color:#cfcfcf}
.product span{display:block;margin-top:22px;font-size:17px;font-weight:600}
.footer{position:absolute;top:2810px;left:0;width:1200px;height:286px;background:var(--night)}
.footer .brand{position:absolute;left:470px;top:60px}
.footer-nav{position:absolute;top:160px;left:132px;width:936px;display:flex;justify-content:space-between}
.footer-nav a{font-size:13px;font-weight:600;color:var(--white);text-decoration:none}
.footer-rule{position:absolute;top:200px;left:132px;width:936px;height:1px;background:var(--gold)}
.copyright{position:absolute;top:230px;left:0;width:1200px;text-align:center;font-size:12px;color:var(--grey)}
</style>
</head>
<body>
<div class="page">
  <div class="topbar">Affordable IT Solutions That Revolutionize Tomorrow's Air Cargo Today</div>

  <section class="hero">
    <div class="earth" role="img" aria-label="Night view of planet Earth with glowing city lights and flight routes"></div>
    <div class="hero-copy">
      <h1>Seamlessly connecting the <em>air cargo industry</em> from Manila to Tahiti!</h1>
      <p>Blending decades of air cargo knowledge with end-to-end IT solutions. Whether you are an Airline, GSA, GHA, Forwarder or E-commerce Operator, our expertise can elevate your daily workflow, cutting down on expenses, time, and errors.</p>
      <a class="btn-gold">LEARN MORE</a>
    </div>
    <div class="play"><svg width="26" height="28" viewBox="0 0 26 28"><path d="M2 2 L24 14 L2 26 Z" fill="#f7c600"/></svg></div>
    <div class="play-label">Play Now</div>
  </section>

  <header class="header">
    <div class="brand"><span class="brand-mark"></span>Brixton Vale</div>
    <a class="btn-outline">CONTACT US</a>
  </header>
  <nav class="nav">
    <a class="active">HOME</a><a>INDUSTRIES</a><a>SOLUTIONS</a><a>OPERATIONAL SUPPORT</a><a>CASE STUDIES</a><a>TESTIMONIALS</a><a>NEWS</a><a>ABOUT US</a>
  </nav>

  <p class="statement">We are not IT tech experts attempting to do cargo! We are cargo<br>experts with programming skills!</p>
  <h2 class="facts-title">FACTS:</h2>
  <div class="facts">
    <div class="fact"><b>2014</b><span>Established:</span></div>
    <div class="fact"><b>18</b><span>Countries covered:</span></div>
    <div class="fact"><b>22</b><span>Employees:</span></div>
    <div class="fact"><b>20+</b><span>Connected Clients:</span></div>
    <div class="fact"><b>11,500,000 +</b><span>Nr. of Annual Electronic Exchanges:</span></div>
    <div class="fact"><b>350,000 +</b><span>Nr. of Annual AWBs:</span></div>
  </div>

  <div class="iso-art" role="img" aria-label="Isometric illustration of cargo boxes, pallets and aircraft moving along a blue logistics grid"></div>
  <section class="about">
    <h2>ABOUT <strong>BRIXTON VALE</strong></h2>
    <p>Stratus is a desktop system for air cargo handling. It covers and automates the entire loading and unloading process. Contains full integration of the ACMA C-IMP messaging process, where cover all parts of ACMA e-freight project.</p>
    <a class="btn-gold">LEARN MORE</a>
  </section>

  <h2 class="solutions-title">SOLUTIONS <strong>STRATUS FAMILY</strong>
    <svg style="display:block;margin:2px auto 0" width="140" height="14" viewBox="0 0 140 14"><path d="M4 10 Q70 0 136 10" stroke="#f7c600" stroke-width="4" fill="none" stroke-linecap="round"/></svg>
  </h2>
  <div class="products">
    <div class="product"><div class="product-icon"><svg width="70" height="70" viewBox="0 0 24 24"><path d="M21 16v-2l-8-5V3.5a1.5 1.5 0 0 0-3 0V9l-8 5v2l8-2.5V19l-2 1.5V22l3.5-1 3.5 1v-1.5L13 19v-5.5z" fill="#111" transform="rotate(45 12 12)"/></svg></div><span>Stratus Airline</span></div>
    <div class="product"><div class="product-icon alt"><svg width="70" height="70" viewBox="0 0 24 24"><path d="M2 10 L12 4 L22 10 V21 H2 Z" fill="none" stroke="#111" stroke-width="1.6"/><path d="M6 12h12M6 15h12M6 18h12" stroke="#111" stroke-width="1.6"/></svg></div><span>Stratus GHA</span></div>
    <div class="product"><div class="product-icon"><svg width="70" height="70" viewBox="0 0 24 24"><rect x="7" y="5" width="10" height="12" fill="none" stroke="#111" stroke-width="1.6"/><path d="M4 3h3M7 17h13" stroke="#111" stroke-width="1.6"/><circle cx="9" cy="20" r="1.6" fill="#111"/><circle cx="17" cy="20" r="1.6" fill="#111"/></svg></div><span>WaybillDesk</span></div>
    <div class="product"><div class="product-icon alt"><svg width="74" height="70" viewBox="0 0 26 24"><rect x="1" y="6" width="15" height="11" fill="none" stroke="#111" stroke-width="1.6"/><path d="M16 10h5l4 4v3h-9z" fill="none" stroke="#111" stroke-width="1.6"/><circle cx="6" cy="19" r="2" fill="#111"/><circle cx="20" cy="19" r="2" fill="#111"/></svg></div><span>StratoTrucks</span></div>
    <div class="product"><div class="product-icon"><svg width="70" height="70" viewBox="0 0 24 24"><path d="M2 4h3l2.5 11h11L21 7H6.5" fill="none" stroke="#111" stroke-width="1.6"/><circle cx="9" cy="19" r="1.6" fill="#111"/><circle cx="17" cy="19" r="1.6" fill="#111"/></svg></div><span>Hive-online</span></div>
  </div>

  <footer class="footer">
    <div class="brand"><span class="brand-mark"></span>Brixton Vale</div>
    <nav class="footer-nav"><a>HOME</a><a>INDUSTRIES</a><a>SOLUTIONS</a><a>OPERATIONAL SUPPORT</a><a>CASE STUDIES</a><a>TESTIMONIALS</a><a>NEWS</a><a>ABOUT US</a></nav>
    <div class="footer-rule"></div>
    <p class="copyright">Copyright © 2024. All Rights Reserved</p>
  </footer>
</div>
</body>
</html>
```